New young doctors office business card

Doctor's office
Hello:
My name is Dr. Mateo Anselmo Quiroga Benítez. I need a business card for my new office located within a hospital. The name of the hospital is "Hospital Almendral". Although the hospital logo and name must be included in the business card, please make me a personal logo for myself. The logo might be maybe my name in a stylish font, or my initials (MAQB) or something like that. Im more inclined to a font logo, rather than a image logo, but a good one might change my mind. The info on my business card is going to be in spanish. The following info must be included please (the info within parenthesis is not to be included, it is provided for you to understand it since it's in spanish, so you can properly place it on the card):
-Dr. Mateo Anselmo Quiroga Benítez (my name)
-Medicina general (My specialty)
-Hospital Almendral (The name of the hospital where my office is)
-Calle Tomás Ibarrola #527 Col. Peñascal (address)
-Tel 471-5836 (Office phone)
-Sábado y domingo 10:00 am a 10:00pm (Office hours)
-Emergencias: 613-907-5148 (Emergency phone)
-mateoqb@correoandino.net (email)
-English Spoken
So, that's all the info i need to be on the business card. Although it's a business card for a doctor's office, i dont want it to be a boring, plain business card. Make it eye-catchy and stylish please. As i said, the hospital logo must be included. You'll find it on the heading of the PDF file i attached, but dont make it the center of attention.
Physician
Hello:My name is Dr. Mateo Anselmo Quiroga Benítez. I need a business card for my new office located within a hospital. The name of the hospital is "Hospital Almendral". Although the hospital logo and name must be included in the business card, please make me a personal logo for myself. The logo might be maybe my name in a stylish font, or my initials (MAQB) or something like that. Im more inclined to a font logo, rather than a image logo, but a good one might change my mind. The info on my business card is going to be in spanish. The following info must be included please (the info within parenthesis is not to be included, it is provided for you to understand it since it's in spanish, so you can properly place it on the card):-Dr. Mateo Anselmo Quiroga Benítez (my name)-Medicina general (My specialty)-Hospital Almendral (The name of the hospital where my office is)-Calle Tomás Ibarrola #527 Col. Peñascal (address)-Tel 471-5836 (Office phone)-Sábado y domingo 10:00 am a 10:00pm (Office hours)-Emergencias: 613-907-5148 (Emergency phone)-mateoqb@correoandino.net (email)-English Spoken So, that's all the info i need to be on the business card. Although it's a business card for a doctor's office, i dont want it to be a boring, plain business card. Make it eye-catchy and stylish please. As i said, the hospital logo must be included. You'll find it on the heading of the PDF file i attached, but dont make it the center of attention.

```html
<!DOCTYPE html>
<html lang="es">
<head>
<meta charset="utf-8">
<title>Tarjeta de presentación – Dr. Mateo Anselmo Quiroga Benítez</title>
<link href="https://fonts.googleapis.com/css2?family=Roboto:wght@300;400;500&display=swap" rel="stylesheet">
<style>
  :root {
    --navy: #173a66;
    --navy-soft: #3d5f8c;
    --slate: #4a6890;
    --grey-mark: #8a96a6;
    --ink: #555b63;
    --ink-light: #7a8088;
    --paper: #ffffff;
    --backdrop: #d9dadc;
  }
  * { margin: 0; padding: 0; box-sizing: border-box; }
  html, body {
    width: 1200px; height: 900px; overflow: hidden;
    background: var(--backdrop);
    font-family: "Roboto", Arial, sans-serif;
  }
  .stage { position: relative; width: 1200px; height: 900px; }

  .card {
    position: absolute; top: 295px;
    width: 540px; height: 310px;
    box-shadow: 0 6px 18px rgba(0,0,0,0.18);
  }
  .card--front { left: 40px; background: linear-gradient(160deg, var(--navy) 55%, #2a4d7c 100%); }
  .card--back { left: 620px; background: var(--paper); }

  /* identity lockup */
  .identity { position: absolute; display: flex; align-items: center; gap: 12px; }
  .identity__mark { width: 30px; height: 30px; flex: none; }
  .identity__rule { width: 1px; height: 52px; }
  .identity__name {
    font-weight: 500; font-size: 15px; line-height: 1.3;
    letter-spacing: 0.06em; text-transform: uppercase;
  }
  .card--front .identity { left: 50%; top: 50%; transform: translate(-50%, -50%); }
  .card--front .identity__mark { background: #c9d0da; }
  .card--front .identity__rule { background: rgba(255,255,255,0.55); }
  .card--front .identity__name { color: #ffffff; }

  .card--back .identity { left: 84px; top: 40px; }
  .card--back .identity__mark { background: var(--grey-mark); }
  .card--back .identity__rule { background: #b7bec8; }
  .card--back .identity__name { color: var(--slate); }

  /* contact block */
  .contact { position: absolute; left: 52px; top: 150px; }
  .contact__name { font-weight: 500; font-size: 15px; color: var(--slate); }
  .contact__role { font-weight: 300; font-size: 13px; color: var(--ink-light); margin-bottom: 10px; }
  .contact__list { list-style: none; }
  .contact__item {
    display: flex; align-items: center; gap: 8px;
    font-weight: 300; font-size: 12.5px; color: var(--ink); line-height: 19px;
  }
  .contact__icon { width: 11px; height: 11px; fill: var(--slate); flex: none; }

  /* hospital */
  .hospital { position: absolute; right: 38px; bottom: 28px; text-align: right; }
  .hospital__head { display: flex; align-items: center; justify-content: flex-end; gap: 8px; }
  .hospital__mark { width: 18px; height: 18px; background: var(--navy); }
  .hospital__name, .hospital__note { font-weight: 300; font-size: 13.5px; color: var(--ink); }
</style>
</head>
<body>
<main class="stage">

  <section class="card card--front" aria-label="Frente de la tarjeta">
    <div class="identity">
      <span class="identity__mark"></span>
      <span class="identity__rule"></span>
      <p class="identity__name">Dr. Mateo Anselmo<br>Quiroga Benítez</p>
    </div>
  </section>

  <section class="card card--back" aria-label="Reverso de la tarjeta">
    <div class="identity">
      <span class="identity__mark"></span>
      <span class="identity__rule"></span>
      <p class="identity__name">Dr. Mateo Anselmo<br>Quiroga Benítez</p>
    </div>

    <div class="contact">
      <p class="contact__name">Dr. Mateo Anselmo Quiroga Benítez</p>
      <p class="contact__role">Medicina general</p>
      <ul class="contact__list">
        <li class="contact__item">
          <svg class="contact__icon" viewBox="0 0 24 24"><path d="M6.6 10.8a15.1 15.1 0 0 0 6.6 6.6l2.2-2.2a1 1 0 0 1 1-.25 11.4 11.4 0 0 0 3.6.57 1 1 0 0 1 1 1V20a1 1 0 0 1-1 1A17 17 0 0 1 3 4a1 1 0 0 1 1-1h3.5a1 1 0 0 1 1 1c0 1.25.2 2.45.57 3.57a1 1 0 0 1-.25 1z"/></svg>
          471-5836
        </li>
        <li class="contact__item">
          <svg class="contact__icon" viewBox="0 0 24 24"><path d="M2 5h20v14H2z M4 7v.5l8 5 8-5V7l-8 5z" fill-rule="evenodd"/></svg>
          mateoqb@correoandino.net
        </li>
        <li class="contact__item">
          <svg class="contact__icon" viewBox="0 0 24 24"><path d="M12 2a7 7 0 0 0-7 7c0 5.2 7 13 7 13s7-7.8 7-13a7 7 0 0 0-7-7zm0 9.5A2.5 2.5 0 1 1 12 6.5a2.5 2.5 0 0 1 0 5z"/></svg>
          Calle Tomás Ibarrola #527 Col. Peñascal
        </li>
        <li class="contact__item">
          <svg class="contact__icon" viewBox="0 0 24 24"><path d="M2 9c2-3 6-4 10-4s8 1 10 4l-3 3-3-2V8H8v2l-3 2z M6 13h12l2 8H4z"/></svg>
          Emergencias: 613-907-5148
        </li>
      </ul>
    </div>

    <div class="hospital">
      <div class="hospital__head">
        <span class="hospital__mark"></span>
      </div>
      <p class="hospital__name">Hospital Almendral</p>
      <p class="hospital__note">English Spoken</p>
    </div>
  </section>

</main>
</body>
</html>
```